Dunmore IT Services needs to look professional and modern

This is my first time using this site so I am unsure what to expect, I am very serious in needing design work done and have no issues paying for it. I am hoping for good things as my business needs this before I can make any money !
Dunmore IT Services Pty Ltd core business is small / medium business networking, support and related hardware ie servers, PC's, Laptops, network equipment/infrastructure, printers etc
The focus of the business to give our customers a competitive edge over others by using new and innovative technologies and services. This is always balanced against stability, reliability and efficiency of the customers IT network.
We are looking for the design of a logo and business cards (there is also the potential for a website once this project is successfully completed). The design should have a sense of refinement and stability while being modern. The choice of colour pallet is up to the designer but nothing gordy.
The cards need to be double sided with the reverse to include brief points of business offered, details of points to be filled in by me later.
The front needs to include business name, mobile number (0471 392 508), my name (Rob Dunmore), email address (rob@DunmoreITServices.com.au), website address (www.DunmoreITServices.com.au), business slogan ("Your Competitive Edge")
Business
"Your Competitive Edge"
Designer to choose colors to be used in the design.

```html
<!DOCTYPE html>
<html lang="en">
<head>
<meta charset="utf-8">
<title>Dunmore IT Services – Business Cards</title>
<link rel="stylesheet" href="https://fonts.googleapis.com/css2?family=Open+Sans:wght@400;700&display=swap">
<style>
  :root {
    --backdrop: #717170;
    --card: #ffffff;
    --tint: #f4f4f4;
    --brand-blue: #2a79b5;
    --brand-orange: #ef7d1a;
    --ink-grey: #6b6b6b;
    --name-grey: #7a7a7a;
    --shadow: rgba(0, 0, 0, 0.28);
  }
  * { margin: 0; padding: 0; box-sizing: border-box; }
  html, body {
    width: 1200px;
    height: 901px;
    overflow: hidden;
    background: var(--backdrop);
    font-family: "Open Sans", Arial, sans-serif;
  }
  .stage {
    position: relative;
    width: 1200px;
    height: 901px;
  }
  .card {
    position: absolute;
    width: 640px;
    height: 366px;
    background: var(--card);
    box-shadow: 6px 10px 24px var(--shadow);
    overflow: hidden;
  }
  .card--front { left: 110px; top: 120px; z-index: 2; }
  .card--back  { left: 450px; top: 420px; z-index: 1; }

  .card__tint {
    position: absolute;
    left: -120px;
    top: 110px;
    width: 300px;
    height: 300px;
    border-radius: 50%;
    background: var(--tint);
  }

  .holder {
    position: absolute;
    left: 262px;
    top: 40px;
    color: var(--name-grey);
    line-height: 1.25;
  }
  .holder__name { font-size: 15px; font-weight: 700; display: block; }
  .holder__role { font-size: 14px; font-weight: 400; display: block; padding-left: 34px; }

  .brand {
    position: absolute;
    left: 232px;
    top: 160px;
    display: flex;
    align-items: center;
    gap: 12px;
  }
  .brand__mark {
    width: 20px;
    height: 20px;
    background: var(--brand-orange);
    border-radius: 3px;
    flex: none;
  }
  .brand__name {
    font-size: 26px;
    font-weight: 700;
    color: var(--brand-blue);
    letter-spacing: 0.3px;
    text-transform: uppercase;
    white-space: nowrap;
  }

  .contact {
    position: absolute;
    left: 330px;
    top: 222px;
    list-style: none;
    font-size: 14px;
    line-height: 1.4;
    color: var(--ink-grey);
  }

  .services {
    position: absolute;
    left: 300px;
    top: 110px;
    list-style: none;
  }
  .services__item {
    display: flex;
    align-items: center;
    gap: 12px;
    font-size: 24px;
    font-weight: 700;
    color: var(--brand-blue);
    line-height: 1.15;
  }
  .services__item::before {
    content: "";
    width: 13px;
    height: 13px;
    border-radius: 2px;
    background: var(--brand-orange);
    flex: none;
  }
</style>
</head>
<body>
  <main class="stage">
    <section class="card card--front" aria-label="Business card front">
      <span class="card__tint" aria-hidden="true"></span>
      <p class="holder">
        <span class="holder__name">Arun Mehta,</span>
        <span class="holder__role">Director</span>
      </p>
      <div class="brand">
        <span class="brand__mark" aria-hidden="true"></span>
        <span class="brand__name">Dunmore IT Services</span>
      </div>
      <ul class="contact">
        <li>Tel: 0482 615 903</li>
        <li>Fax: 07 5312 4870</li>
        <li>Email: hello@dunmoreitservices.co.in</li>
        <li>dunmoreitservices.co.in</li>
      </ul>
    </section>

    <section class="card card--back" aria-label="Business card back">
      <span class="card__tint" aria-hidden="true"></span>
      <ul class="services">
        <li class="services__item">Servers</li>
        <li class="services__item">Networks</li>
        <li class="services__item">PC's</li>
      </ul>
    </section>
  </main>
</body>
</html>
```